Titlescreen rework for real estate homepage

Hello, this is my homepage (http://www.wolde-immobilien.de) and I am just looking for a title page for the title screen. So I guess the main target is finding a fitting picture for it. Re-arranging the menu is not a must, but I at the open everything even for new Ideas of additional elements. The rest of the homepage stays as it is. What I'm looking for is taff to describe, I already needed a long time finding the current picture. I am a real estate agent so it should have a link to estates. It could be a dark theme as it now or maybe something more light with "white" in it as you can scroll down. Of course it should work with the elements appearing bottom. Because I do not work in New York, just in a smaller area in Germany, no scyscrappers to find. I hope someone can show up with a new and fitting new title screen for me. I uploaded the logo-file for you to build in. The used font is raleway, cause its used in the logo as well. Its downloadable here: (https://www.typeorchard.com/fonts/raleway)
Target Market(s)
Real-Estate
Industry/Entity Type
Real Estate
Number of Pages Required
1 page
Look and feel

```html
<!DOCTYPE html>
<html lang="de">
<head>
<meta charset="utf-8">
<title>WOLDE Immobilien – Startseite</title>
<link href="https://fonts.googleapis.com/css2?family=Raleway:wght@400;500;600;700&display=swap" rel="stylesheet">
<style>
  :root {
    --white: #ffffff;
    --text-dark: #1c1c1c;
    --button-bg: #f4f4f4;
    --dot-inactive: rgba(255, 255, 255, 0.45);
    --sky-top: #3b3e43;
    --sky-mid: #4a4b4d;
    --town-warm: #6b4a37;
    --town-dark: #2a2320;
    --glow: rgba(214, 128, 70, 0.55);
  }
  * { margin: 0; padding: 0; box-sizing: border-box; }
  html, body {
    width: 1200px;
    height: 670px;
    overflow: hidden;
    font-family: "Raleway", sans-serif;
    color: var(--white);
    background: var(--town-dark);
  }
  .title-screen {
    position: relative;
    width: 1200px;
    height: 670px;
    overflow: hidden;
  }
  .hero-photo {
    position: absolute;
    inset: 0;
    background:
      radial-gradient(ellipse 420px 220px at 760px 560px, var(--glow), transparent 70%),
      linear-gradient(180deg, var(--sky-top) 0%, var(--sky-mid) 55%, var(--town-warm) 78%, var(--town-dark) 100%);
  }
  .brand {
    position: absolute;
    top: 86px;
    left: 0;
    width: 100%;
    text-align: center;
    font-size: 19px;
    font-weight: 500;
    letter-spacing: 0.2px;
  }
  .main-nav {
    position: absolute;
    top: 153px;
    left: 0;
    width: 100%;
    display: flex;
    justify-content: center;
    gap: 27px;
    list-style: none;
  }
  .main-nav a {
    color: var(--white);
    text-decoration: none;
    font-size: 11px;
    font-weight: 500;
    letter-spacing: 0.2px;
    display: inline-block;
    padding-bottom: 5px;
  }
  .main-nav a.is-active {
    font-weight: 700;
    border-bottom: 1px solid var(--white);
  }
  .hero-heading {
    position: absolute;
    top: 286px;
    left: 0;
    width: 100%;
    text-align: center;
  }
  .hero-title {
    font-size: 50px;
    font-weight: 500;
    line-height: 1.05;
    letter-spacing: 0.5px;
  }
  .hero-subtitle {
    font-size: 25px;
    font-weight: 400;
    line-height: 1.2;
    margin-top: 2px;
  }
  .cta-button {
    position: absolute;
    top: 437px;
    left: 488px;
    width: 224px;
    height: 48px;
    border-radius: 24px;
    background: var(--button-bg);
    color: var(--text-dark);
    font-size: 11.5px;
    font-weight: 700;
    letter-spacing: 0.3px;
    text-decoration: none;
    display: flex;
    align-items: center;
    justify-content: center;
  }
  .slide-dots {
    position: absolute;
    top: 297px;
    left: 1154px;
    list-style: none;
    display: flex;
    flex-direction: column;
    gap: 9px;
  }
  .slide-dots li {
    width: 10px;
    height: 10px;
    border-radius: 50%;
    background: var(--dot-inactive);
  }
  .slide-dots li.is-current { background: var(--white); }
  .scroll-hint {
    position: absolute;
    top: 586px;
    left: 0;
    width: 100%;
    display: flex;
    flex-direction: column;
    align-items: center;
    font-size: 11.5px;
    font-weight: 500;
    letter-spacing: 0.3px;
  }
  .scroll-hint svg { display: block; margin-bottom: 14px; }
</style>
</head>
<body>
  <header class="title-screen">
    <div class="hero-photo" role="img" aria-label="Abendlicher Blick über die Dächer einer historischen Kleinstadt mit Kirchturm und Marktplatz, warmes Gegenlicht"></div>

    <div class="brand">WOLDE Immobilien</div>

    <nav>
      <ul class="main-nav">
        <li><a class="is-active" href="#">STARTSEITE</a></li>
        <li><a href="#">VERKAUFEN</a></li>
        <li><a href="#">IMMOBILIEN</a></li>
        <li><a href="#">INFOS</a></li>
        <li><a href="#">SERVICE</a></li>
        <li><a href="#">PARTNER</a></li>
        <li><a href="#">KONTAKT</a></li>
      </ul>
    </nav>

    <div class="hero-heading">
      <h1 class="hero-title">WOLDE IMMOBILIEN</h1>
      <p class="hero-subtitle">IHR MARKLER IM NORDEN</p>
    </div>

    <a class="cta-button" href="#">HERZLICH WILLKOMMEN</a>

    <ul class="slide-dots">
      <li class="is-current"></li>
      <li></li>
      <li></li>
      <li></li>
    </ul>

    <div class="scroll-hint">
      <svg width="18" height="42" viewBox="0 0 18 42" aria-hidden="true">
        <rect x="1" y="1" width="16" height="29" rx="8" fill="none" stroke="#fff" stroke-width="1.3"/>
        <line x1="9" y1="6" x2="9" y2="11" stroke="#fff" stroke-width="1.3" stroke-linecap="round"/>
        <polyline points="4,35 9,39 14,35" fill="none" stroke="#fff" stroke-width="1.3"/>
      </svg>
      <span>SCROLLEN</span>
    </div>
  </header>
</body>
</html>
```